Website Redesign for Technology Focused Investment Bank

We need a website redesign for a technology and digital media focused investment banking firm. Think modern and forward thinking yet stable and smart. We provide mergers and acquisitions advisory services to our clients. Our target market are CEO's and CFO's (senior executives) that run and operate technology firms.

Kestrel Bay Advisors - www.kestrelbayadvisors.example

We are headquartered in Los Angeles, CA. Please do NOT use the Brindle Arch for anything.

We have the content and can update the photos as well.

We are looking for a "template" website we can update and edit with ease.

A competitive firm's website is: www.dunmoregrey.example Not sure I like it but I want it to look way better then this one.

Looking for a more modern version. Not too stuffy and conservative, please. Elegant, smart, updated and progressive/modern.
Updates

Color preferences:  Blue's including matching logo color. Grey's. You can add other colors if it flows well and looks clean and nice.

Menu:  Drop Down

Open to platform...please use one that most people can use, is reasonably priced if I need to buy it, and easy to update monthly and sometimes weekly.

Please use this website as a good example of what we are looking for (or similar version of it): www.plorvex.example

Thanks!
Tobias R.

We are reviewing all submissions and will select one this week. Thank you everyone for your outstanding and creative designs you have sent us. We really appreciate it.

Thanks for everyone's hard work and creative input into our website design. We really appreciate it!

Target Market(s)

CEO's and CFO's, Entrepreneurs and Board Members of Technology Companies.

Industry/Entity Type

Investment

Font styles to use
Sans Serif

Colors
33a6d7
0492cd
0555a3
3176b5
85abd2
333333
5c5c5c
757575

Requirements
Must have
• Links to social media including Twitter, LinkedIn, Google+, Facebook, etc.

Must try to match logo color
Should not have
• No conservative, old looking colors or background. For example, no green marble look.

```html
<!DOCTYPE html>
<html lang="en">
<head>
<meta charset="utf-8">
<title>Kestrel Bay Advisors</title>
<link rel="stylesheet" href="https://fonts.googleapis.com/css2?family=Open+Sans:wght@400;600&family=Roboto+Condensed:wght@400;700&display=swap">
<style>
:root{
  --blue:#0555a3;
  --blue-mid:#3176b5;
  --sky:#33a6d7;
  --sky-light:#85c9ea;
  --ink:#333333;
  --text:#5c5c5c;
  --muted:#757575;
  --band-grey:#f2f2f2;
  --band-sky:#cfe6f4;
  --footer:#0b1f55;
  --footer-line:#1c3470;
  --white:#ffffff;
}
*{box-sizing:border-box;margin:0;padding:0}
html,body{width:800px;height:1200px;overflow:hidden}
body{position:relative;background:linear-gradient(#f3f3f3 0,#fff 110px);font-family:"Open Sans",sans-serif;color:var(--text)}
.abs{position:absolute}
.header{left:94px;top:12px;width:612px;height:70px;background:var(--white);box-shadow:0 0 4px rgba(0,0,0,.15)}
.brand{left:12px;top:14px;display:flex;align-items:center;gap:10px}
.brand-dot{width:38px;height:38px;border-radius:50%;background:var(--blue-mid)}
.brand-name{font-family:"Roboto Condensed",sans-serif;font-size:22px;color:var(--blue);font-weight:400}
.top-links{right:106px;top:13px;font-size:10px;color:var(--ink);display:flex;gap:13px}
.lang{right:6px;top:8px;width:76px;height:22px;background:var(--blue);color:#fff;font-size:10px;line-height:22px;padding-left:8px;border-radius:2px}
.search{right:6px;top:40px;width:149px;height:23px;background:#eeeeee;font-size:10px;color:#999;line-height:23px;padding-left:8px}
.search svg{position:absolute;right:6px;top:5px}
.nav{left:94px;top:82px;width:612px;height:28px;display:flex;gap:2px;background:var(--white)}
.nav span{background:var(--blue);color:#fff;font-family:"Roboto Condensed",sans-serif;font-size:10.5px;line-height:28px;text-align:center;flex:auto}
.hero{left:94px;top:111px;width:612px;height:281px;background:linear-gradient(180deg,#8a99a6 0%,#c8d2d9 35%,#6b5e55 70%,#3e3430 100%)}
.hero-title{left:94px;top:155px;width:612px;text-align:center;font-family:"Roboto Condensed",sans-serif;font-weight:700;font-size:30px;line-height:32px;color:#fff;letter-spacing:.2px}
.section-title{font-family:"Roboto Condensed",sans-serif;color:var(--blue);font-size:20px}
.services-title{left:0;width:800px;top:406px;text-align:center}
.service{width:150px;text-align:center;top:447px}
.service .ring{width:64px;height:64px;margin:0 auto;border-radius:50%;background:#fff;box-shadow:0 0 3px rgba(0,0,0,.25);display:flex;align-items:center;justify-content:center}
.service .disc{width:56px;height:56px;border-radius:50%;background:var(--sky-light);display:flex;align-items:center;justify-content:center}
.service .disc.dark{background:var(--blue)}
.service p{font-family:"Roboto Condensed",sans-serif;font-size:13px;color:var(--ink);margin-top:8px}
.rule{left:94px;top:572px;width:612px;height:3px;background:#eeeeee}
.why-photo{left:94px;top:600px;width:120px;height:131px;border:4px solid #fff;box-shadow:0 0 3px rgba(0,0,0,.3);background:linear-gradient(160deg,#c9d6e2,#8c9aa8 55%,#4d5560)}
.why{left:226px;top:596px;width:305px}
.body-text{font-size:9.5px;line-height:14.5px;color:var(--text)}
.why .body-text{margin-top:8px}
.why .body-text+.body-text{margin-top:13px}
a,.link{color:var(--blue-mid);text-decoration:none}
.more{font-size:9.5px;margin-top:10px;display:block}
.news{left:549px;top:596px;width:160px}
.news-item{margin-top:7px}
.news-item:first-of-type{margin-top:8px}
.news-date{font-size:9.5px;color:var(--blue-mid);padding-left:10px;position:relative}
.news-date::before{content:"+";position:absolute;left:0;color:var(--muted);font-size:8px}
.news-item .body-text{padding-left:10px;margin-top:4px}
.clients{left:0;top:779px;width:800px;height:89px;background:var(--band-grey)}
.client{top:813px;font-family:"Roboto Condensed",sans-serif;font-weight:700;font-size:21px;color:#bcbcbc;letter-spacing:.5px}
.tweet{left:0;top:868px;width:800px;height:117px;background:var(--band-sky)}
.handle{left:0;width:800px;top:890px;text-align:center;font-size:10px;color:var(--blue-mid)}
.tweet-dot{left:130px;top:910px;width:30px;height:30px;border-radius:50%;background:var(--blue-mid)}
.tweet-text{left:170px;top:909px;width:460px;text-align:center;font-size:9.5px;line-height:14px;color:var(--text)}
.pager{left:373px;top:951px;display:flex;gap:4px}
.pager i{width:8px;height:8px;border-radius:50%;background:#fff}
.pager i:first-child{background:var(--blue)}
.footer{left:0;top:985px;width:800px;height:215px;background:var(--footer)}
.fcol-line{top:985px;width:1px;height:135px;background:var(--footer-line)}
.ftitle{font-family:"Roboto Condensed",sans-serif;font-size:14px;color:#fff}
.ftext{font-size:9.5px;line-height:16px;color:#cdd6ea}
.newsletter{left:93px;top:1005px}
.email-box{left:94px;top:1058px;width:130px;height:24px;background:#fff;font-size:9.5px;color:#888;line-height:24px;padding-left:6px}
.send{left:224px;top:1058px;width:61px;height:24px;background:var(--sky);color:#fff;font-size:11px;font-weight:600;display:flex;align-items:center;gap:5px;padding-left:6px}
.follow{left:346px;top:1005px}
.socials{left:346px;top:1031px;display:flex;gap:4px}
.socials i{width:23px;height:23px;border:1px solid #fff}
.contact{left:508px;top:1005px;width:210px}
.flinks{left:94px;top:1131px;width:612px;display:flex;justify-content:space-between;font-size:9.5px;color:#fff}
.fline{left:94px;top:1155px;width:612px;height:1px;background:var(--footer-line)}
.copy{left:0;width:800px;top:1172px;text-align:center;font-size:8px;color:#cdd6ea}
</style>
</head>
<body>

<header class="abs header">
  <div class="abs brand"><span class="brand-dot"></span><span class="brand-name">Kestrel Bay Advisors</span></div>
  <nav class="abs top-links"><span>Home</span><span>About Us</span><span>Contact Us</span></nav>
  <div class="abs lang">Language &#9662;</div>
  <div class="abs search">Search here...
    <svg width="13" height="13" viewBox="0 0 13 13"><circle cx="5.5" cy="5.5" r="4" fill="none" stroke="#999" stroke-width="1.5"/><line x1="8.5" y1="8.5" x2="12" y2="12" stroke="#999" stroke-width="1.8"/></svg>
  </div>
</header>

<nav class="abs nav">
  <span>SERVICES</span><span>TRANSACTIONS</span><span>RESEARCH</span><span>PRIVATE EQUITY</span><span>RECOMMENDATIONS</span><span>ABOUT THE FOUNDER</span><span>CAREERS</span><span>NEWS &amp; BLOG</span>
</nav>

<div class="abs hero" role="img" aria-label="Photo of a modern boardroom with a long conference table and tall windows"></div>
<h1 class="abs hero-title">TECHNOLOGY AND DIGITAL MEDIA<br>INVESTMENT BANKING</h1>

<h2 class="abs section-title services-title">Our Services</h2>

<div class="abs service" style="left:69px">
  <div class="ring"><div class="disc dark">
    <svg width="30" height="30" viewBox="0 0 30 30"><rect x="6" y="12" width="18" height="14" rx="2" fill="#fff"/><circle cx="15" cy="11" r="8" fill="#fff" stroke="#0555a3" stroke-width="2"/><circle cx="15" cy="11" r="3" fill="#0555a3"/></svg>
  </div></div><p>Software</p>
</div>
<div class="abs service" style="left:239px">
  <div class="ring"><div class="disc">
    <svg width="30" height="30" viewBox="0 0 30 30"><line x1="7" y1="23" x2="22" y2="8" stroke="#fff" stroke-width="4" stroke-linecap="round"/><line x1="8" y1="8" x2="23" y2="23" stroke="#fff" stroke-width="3" stroke-linecap="round"/><circle cx="23" cy="7" r="4" fill="none" stroke="#fff" stroke-width="2.5"/></svg>
  </div></div><p>IT Services</p>
</div>
<div class="abs service" style="left:410px">
  <div class="ring"><div class="disc">
    <svg width="32" height="32" viewBox="0 0 32 32"><circle cx="16" cy="16" r="12" fill="none" stroke="#fff" stroke-width="2.5"/><ellipse cx="16" cy="16" rx="5" ry="12" fill="none" stroke="#fff" stroke-width="2"/><line x1="4" y1="16" x2="28" y2="16" stroke="#fff" stroke-width="2"/></svg>
  </div></div><p>Internet &amp; Digital Media</p>
</div>
<div class="abs service" style="left:580px">
  <div class="ring"><div class="disc">
    <svg width="30" height="30" viewBox="0 0 30 30"><rect x="9" y="3" width="12" height="24" rx="2" fill="#fff"/><rect x="11" y="6" width="8" height="8" fill="#85c9ea"/><g fill="#85c9ea"><rect x="11" y="16" width="2" height="2"/><rect x="14" y="16" width="2" height="2"/><rect x="17" y="16" width="2" height="2"/><rect x="11" y="19" width="2" height="2"/><rect x="14" y="19" width="2" height="2"/><rect x="17" y="19" width="2" height="2"/></g></svg>
  </div></div><p>Mobile</p>
</div>

<div class="abs rule"></div>

<div class="abs why-photo" role="img" aria-label="Photo of a bright modern office lounge"></div>
<section class="abs why">
  <h2 class="section-title">Why Us?</h2>
  <p class="body-text">We are an independent investment bank and M&amp;A advisory firm focused exclusively on the global Technology and Digital Media sectors. Specifically, we execute mergers and acquisitions for the <a href="#">Software</a>, <a href="#">IT Services</a>, <a href="#">Internet and Digital Media</a> industry sectors.</p>
  <p class="body-text">Our professionals have completed over $20 billion in transactions to date and have experience in investment banking.</p>
  <a class="more" href="#">Read more...</a>
</section>

<section class="abs news">
  <h2 class="section-title">Latest News</h2>
  <div class="news-item"><div class="news-date">July, 24 2014</div><p class="body-text">Lorem Ipsum is simply dummy text of the printing and typesetting...</p></div>
  <div class="news-item"><div class="news-date">July, 24 2014</div><p class="body-text">Lorem Ipsum is simply dummy text of the printing and typesetting...</p></div>
  <a class="more" href="#">Read more...</a>
</section>

<div class="abs clients"></div>
<svg class="abs" style="left:92px;top:815px" width="12" height="18" viewBox="0 0 12 18"><polyline points="10,1 2,9 10,17" fill="none" stroke="#bbb" stroke-width="1.5"/></svg>
<span class="abs client" style="left:124px">NORVANE</span>
<span class="abs client" style="left:292px">TALLIS</span>
<span class="abs client" style="left:432px;font-weight:400">quarrymill</span>
<span class="abs client" style="left:548px">BRIGHTLOOM</span>
<svg class="abs" style="left:696px;top:815px" width="12" height="18" viewBox="0 0 12 18"><polyline points="2,1 10,9 2,17" fill="none" stroke="#bbb" stroke-width="1.5"/></svg>

<div class="abs tweet"></div>
<div class="abs handle">@TechMediaDeals</div>
<div class="abs tweet-dot"></div>
<p class="abs tweet-text">Lorem Ipsum is simply dummy text of the printing and typesetting industry. Lorem Ipsum has been the industry's standard dummy text ever since the 1500s...<span class="link">lnk.example/q7Rt</span></p>
<div class="abs pager"><i></i><i></i><i></i><i></i><i></i></div>

<footer class="abs footer"></footer>
<div class="abs fcol-line" style="left:323px"></div>
<div class="abs fcol-line" style="left:481px"></div>

<div class="abs newsletter">
  <h3 class="ftitle">Newsletter!</h3>
  <p class="ftext" style="margin-top:6px">Subscribe to our M&amp;A Quarterly Updates</p>
</div>
<div class="abs email-box">Enter email</div>
<div class="abs send"><svg width="16" height="11" viewBox="0 0 16 11"><rect x="0.5" y="0.5" width="15" height="10" fill="#fff"/><polyline points="0.5,0.5 8,6 15.5,0.5" fill="none" stroke="#33a6d7"/></svg>Send</div>

<div class="abs follow"><h3 class="ftitle">Follow Us</h3></div>
<div class="abs socials">
  <i style="background:#3b5998"></i><i style="background:#3aa0d8"></i><i style="background:#d23b2e"></i><i style="background:#3f86be"></i>
</div>

<div class="abs contact">
  <h3 class="ftitle">Contact Us</h3>
  <p class="ftext" style="margin-top:6px">Kestrel Bay Advisors, LLC<br>4120 Harbor Crest Ave, Suite 300 Los Angeles,<br>CA 90000 United States of America<br>Mobile: +1 (310) 555-0142<br>EMail: <span class="link" style="color:#33a6d7">mergers@kestrelbayadvisors.example</span></p>
</div>

<nav class="abs flinks"><span>Home</span><span>About</span><span>Services</span><span>Transactions</span><span>Research</span><span>Private Equity</span><span>Recommendations</span><span>About the Founder</span><span>Careers</span><span>News &amp; Blog</span></nav>
<div class="abs fline"></div>
<p class="abs copy">Copyright © 2014 Kestrel Bay Advisors. All Rights Reserved.</p>

</body>
</html>
```